Plumbing Company business card design

Create a business card for our plumbing company. Following info needs to be present

Website-prairiepipeworks.com
Email- contact@prairiepipeworks-mail.com
Phone-515-394-2068
Address-4817 NW Cobalt Blvd STE K
Ankeny, Iowa 50347

```html
<!DOCTYPE html>
<html lang="en">
<head>
<meta charset="utf-8">
<title>Prairie Pipeworks business card</title>
<link rel="stylesheet" href="https://fonts.googleapis.com/css2?family=Montserrat:wght@500;600;700&family=Open+Sans:wght@400&display=swap">
<style>
  :root {
    --page: #ffffff;
    --ink: #000000;
    --sky-top: #55d6fd;
    --sky-mid: #2b93f0;
    --sky-deep: #1767e8;
    --chevron: #0b58e6;
    --purple: #5a3fb6;
    --red: #f5192e;
    --white: #ffffff;
    --disc-top: #f3f3f4;
    --disc-bottom: #a9aaad;
    --ring: #2e2e2e;
    --icon: #3cc5f7;
    --brand-red: #f01f32;
  }
  * { margin: 0; padding: 0; box-sizing: border-box; }
  html, body { width: 1200px; height: 1200px; overflow: hidden; background: var(--page); }
  .sheet { position: relative; width: 1200px; height: 1200px; }

  .side-label {
    position: absolute; left: 0; width: 1200px; text-align: center;
    font-family: "Open Sans", sans-serif; font-weight: 400;
    font-size: 118px; line-height: 1; color: var(--ink); letter-spacing: 2px;
  }
  .side-label--front { top: 12px; }
  .side-label--back { top: 600px; }

  .card {
    position: absolute; left: 255px; width: 719px; height: 420px; overflow: hidden;
    font-family: "Montserrat", sans-serif;
  }
  .card--front { top: 140px; background: linear-gradient(180deg, var(--sky-top) 0%, var(--sky-mid) 45%, var(--sky-deep) 100%); }
  .card--back { top: 722px; background: linear-gradient(90deg, #2158f0 0%, #2a73f5 45%, #3a9af7 80%, var(--sky-top) 100%); }

  .card__art { position: absolute; inset: 0; width: 719px; height: 420px; }

  .company-name {
    position: absolute; top: 18px; left: 0; width: 100%; text-align: center;
    font-weight: 600; font-size: 66px; color: var(--white); letter-spacing: -0.5px;
  }
  .contact {
    position: absolute; top: 135px; left: 0; width: 100%; text-align: center;
    color: var(--white); font-weight: 500;
  }
  .contact__line { font-size: 23px; line-height: 21px; }
  .contact__dots { display: flex; justify-content: center; gap: 7px; margin: 10px 0 9px; }
  .contact__dots span { width: 6px; height: 6px; border-radius: 50%; background: var(--white); }
  .contact__phone { font-size: 23px; line-height: 22px; }
  .contact__email { font-size: 22px; line-height: 22px; }

  .web-badge {
    position: absolute; left: 218px; top: 301px; width: 284px; height: 284px; border-radius: 50%;
    background: linear-gradient(180deg, #f7f7f7, #dcdcdc);
    box-shadow: 0 -2px 8px rgba(0,0,0,0.25);
  }
  .web-badge__ring {
    position: absolute; inset: 13px; border-radius: 50%; border: 4px solid var(--ring);
  }
  .web-badge__icons {
    position: absolute; top: 48px; left: 0; width: 100%;
    display: flex; justify-content: center; gap: 15px;
  }
  .web-badge__icons span { width: 25px; height: 25px; border-radius: 50%; background: var(--icon); }
  .web-badge__url {
    position: absolute; top: 81px; left: 0; width: 100%; text-align: center;
    font-weight: 700; font-size: 19px; color: #111;
  }

  .brand-disc {
    position: absolute; left: 45px; top: 29px; width: 362px; height: 362px; border-radius: 50%;
    background: linear-gradient(180deg, #f4f4f5 0%, #d8d9db 50%, #a0a1a4 100%);
    box-shadow: 0 4px 14px rgba(0,0,0,0.35);
  }
  .brand-disc__ring {
    position: absolute; inset: 14px; border-radius: 50%; border: 5px solid var(--ring);
  }
  .brand-disc__mark {
    position: absolute; left: 50%; top: 108px; width: 60px; height: 60px; margin-left: -30px;
    border-radius: 50%; background: var(--brand-red);
  }
  .brand-disc__name {
    position: absolute; top: 188px; left: 0; width: 100%; text-align: center;
    font-weight: 700; font-size: 34px; line-height: 38px; color: var(--brand-red);
    text-transform: uppercase;
  }
</style>
</head>
<body>
<main class="sheet">
  <h2 class="side-label side-label--front">FRONT</h2>

  <section class="card card--front">
    <svg class="card__art" viewBox="0 0 719 420">
      <defs>
        <linearGradient id="band-left" x1="0" x2="1" y1="0" y2="0">
          <stop offset="0" stop-color="var(--purple)"/>
          <stop offset="1" stop-color="var(--red)"/>
        </linearGradient>
        <linearGradient id="band-right" x1="1" x2="0" y1="0" y2="0">
          <stop offset="0" stop-color="var(--purple)"/>
          <stop offset="0.45" stop-color="var(--red)"/>
          <stop offset="1" stop-color="var(--red)"/>
        </linearGradient>
      </defs>
      <polygon points="0,249 222,395 222,420 0,420" fill="url(#band-left)"/>
      <polygon points="719,249 497,395 497,420 719,420" fill="url(#band-right)"/>
      <polygon points="0,356 174,420 0,420" fill="var(--chevron)" role="img" aria-label="Blue chevron pattern"/>
      <polygon points="719,356 545,420 719,420" fill="var(--chevron)" role="img" aria-label="Blue chevron pattern"/>
    </svg>

    <h1 class="company-name">prairie pipeworks</h1>

    <div class="contact">
      <p class="contact__line">4817 NW Cobalt Blvd STE K</p>
      <p class="contact__line">Ankeny, Iowa 50347</p>
      <div class="contact__dots"><span></span><span></span><span></span></div>
      <p class="contact__phone">515-394-2068</p>
      <div class="contact__dots"><span></span><span></span><span></span></div>
      <p class="contact__email">contact@prairiepipeworks-mail.com</p>
    </div>

    <div class="web-badge">
      <div class="web-badge__ring"></div>
      <div class="web-badge__icons"><span></span><span></span><span></span></div>
      <p class="web-badge__url">prairiepipeworks.com</p>
    </div>
  </section>

  <h2 class="side-label side-label--back">BACK</h2>

  <section class="card card--back">
    <svg class="card__art" viewBox="0 0 719 420">
      <defs>
        <linearGradient id="band-back" x1="0" x2="1" y1="0" y2="0">
          <stop offset="0" stop-color="var(--red)"/>
          <stop offset="1" stop-color="#8a2a6a"/>
        </linearGradient>
      </defs>
      <polygon points="0,0 270,0 150,210 285,420 0,420" fill="var(--chevron)" role="img" aria-label="Blue chevron pattern"/>
      <polygon points="270,0 380,0 230,210 380,420 285,420 150,210" fill="url(#band-back)"/>
    </svg>

    <div class="brand-disc">
      <div class="brand-disc__ring"></div>
      <div class="brand-disc__mark"></div>
      <p class="brand-disc__name">Prairie<br>Pipeworks</p>
    </div>
  </section>
</main>
</body>
</html>
```